Bright Path Therapies business cards and stationary

Need business cards and stationary designed to match previously made logo for for a new company based in Sydney NSW called 'Bright Path Therapies'.

We provide early intervention services and diagnostic assessment for children with disability and their families. I would like designs that are colourful and child friendly - possibly using feet/footprints/steps on a white background. The final design should communicate that we are family friendly, accepting and fun to work with.

Target Market(s)

Parents and Families
Teachers
Allied Health Professionals

Industry/Entity Type

Psychology

Contact Information for Business Card

Bright Path Therapies
www.brightpaththerapies.example
info@brightpaththerapies.example

Font styles to use
Sans Serif
Decorative
Script

Requirements
Must have
• Match the font and colour scheme of logo, along with footprint picture
Nice to have
• Clean and simple, while reflecting that I am working with families.
• Also- editable for when we make staff specific cards.

```html
<!DOCTYPE html>
<html lang="en">
<head>
<meta charset="utf-8">
<title>Bright Path Therapies – Business Cards</title>
<link rel="stylesheet" href="https://fonts.googleapis.com/css2?family=Montserrat:wght@400;500;600&family=Dancing+Script:wght@600&display=swap">
<style>
  :root {
    --bg: #141414;
    --card: #ffffff;
    --red: #ef4136;
    --blue: #1d6fc4;
    --ink: #333333;
    --muted: #555555;
  }
  * { box-sizing: border-box; margin: 0; padding: 0; }
  html, body { width: 1200px; height: 1200px; overflow: hidden; }
  body {
    background: var(--bg);
    font-family: "Montserrat", sans-serif;
    position: relative;
  }
  .card {
    position: absolute;
    left: 220px;
    width: 760px;
    height: 434px;
    background: var(--card);
    overflow: hidden;
    box-shadow: 0 14px 30px rgba(0,0,0,.55);
  }
  .card--front { top: 120px; }
  .card--back { top: 630px; }
  .footprint-band { position: absolute; inset: 0; width: 100%; height: 100%; }
  .brand {
    position: absolute;
    display: flex;
    align-items: center;
    gap: 14px;
  }
  .brand__dot {
    width: 58px; height: 58px;
    border-radius: 50%;
    background: var(--red);
    flex: none;
  }
  .brand__name {
    font-weight: 500;
    color: var(--blue);
    letter-spacing: .5px;
    white-space: nowrap;
  }
  .card--front .brand { left: 70px; top: 190px; }
  .card--front .brand__name { font-size: 34px; }
  .rule {
    position: absolute;
    left: 70px; top: 290px;
    width: 400px; height: 2px;
    background: var(--red);
  }
  .address {
    position: absolute;
    left: 70px; top: 310px;
    font-size: 22px;
    color: var(--ink);
  }
  .card--back .brand { right: 50px; top: 60px; }
  .card--back .brand__name { font-size: 28px; }
  .person {
    position: absolute;
    right: 50px; top: 140px;
    text-align: right;
  }
  .person__name {
    font-family: "Dancing Script", cursive;
    font-size: 40px;
    color: var(--red);
    line-height: 1;
  }
  .person__role { font-size: 16px; color: var(--ink); margin-top: 4px; }
  .contact {
    position: absolute;
    right: 50px; top: 265px;
    list-style: none;
    text-align: right;
    font-size: 16px;
    color: var(--muted);
    line-height: 1.75;
  }
  .contact li { display: flex; justify-content: flex-end; align-items: center; gap: 10px; white-space: nowrap; }
  .contact__icon {
    width: 14px; height: 14px;
    border: 2px solid var(--red);
    border-radius: 3px;
    flex: none;
  }
</style>
</head>
<body>

  <section class="card card--front">
    <svg class="footprint-band" viewBox="0 0 760 434" role="img" aria-label="Band of white footprints walking across red">
      <path fill="var(--red)" d="M440 0 C520 70 560 120 600 200 C640 280 660 360 690 434 L760 434 L760 0 Z"/>
    </svg>
    <div class="brand">
      <span class="brand__dot"></span>
      <span class="brand__name">Bright Path Therapies</span>
    </div>
    <div class="rule"></div>
    <p class="address">Dummy city, Dummy Country Land</p>
  </section>

  <section class="card card--back">
    <svg class="footprint-band" viewBox="0 0 760 434" role="img" aria-label="Band of white footprints walking across red">
      <path fill="var(--red)" d="M0 0 L240 0 C240 90 260 140 290 210 C320 280 330 360 340 434 L0 434 Z"/>
    </svg>
    <div class="brand">
      <span class="brand__dot"></span>
      <span class="brand__name">Bright Path Therapies</span>
    </div>
    <div class="person">
      <p class="person__name">Alex Morgan</p>
      <p class="person__role">Director</p>
    </div>
    <ul class="contact">
      <li>1-555-010-2030 <span class="contact__icon"></span></li>
      <li>www.brightpaththerapies.example <span class="contact__icon"></span></li>
      <li>info@brightpaththerapies.example <span class="contact__icon"></span></li>
    </ul>
  </section>

</body>
</html>
```